Consulting company business cards

We have a base design, but would be willing to update. We have a new logo/"tag" that needs to be added. Current business card design is attached for reference into our "style."

Industry/Entity Type

Business

Contact Information for Business Card

Should contain name and title, office number, mobile number if appropriate, e-mail, website, physical address, and company logo.

Font styles to use
Other font styles liked:
• See current card design on DrovankBCard

Colors
0455a3
85acd3
aaaaaa

Requirements
Must have
• Our colors are navy blue, gray, and a lighter blue
Nice to have
• Design that I can easily drop in new names/titles as we hire employees.

```html
<!DOCTYPE html>
<html lang="en">
<head>
<meta charset="utf-8">
<title>Kestrel Business Cards</title>
<link href="https://fonts.googleapis.com/css2?family=Open+Sans:wght@400;600;700&display=swap" rel="stylesheet">
<style>
  :root {
    --backdrop: #3a332e;
    --card: #111111;
    --card-edge: #1c1c1c;
    --light-blue: #85acd3;
    --navy: #0455a3;
    --gray: #aaaaaa;
    --silver: #c9c9c9;
    --text: #e8e8e8;
    --rule: #3a3a3a;
  }
  * { box-sizing: border-box; margin: 0; padding: 0; }
  html, body {
    width: 1200px; height: 900px; overflow: hidden;
    background: var(--backdrop);
    font-family: "Open Sans", Arial, sans-serif;
  }
  .canvas {
    width: 1200px; height: 900px;
    display: flex; align-items: center; justify-content: center; gap: 40px;
  }
  .card {
    width: 525px; height: 300px;
    background: var(--card);
    border: 1px solid var(--card-edge);
    position: relative;
    box-shadow: 0 14px 30px rgba(0,0,0,.45);
  }
  /* Front */
  .card-front .mark-area {
    position: absolute; left: 0; top: 0; width: 215px; height: 100%;
    display: flex; align-items: center; justify-content: center;
  }
  .mark-dot { width: 120px; height: 120px; border-radius: 50%; background: var(--light-blue); }
  .card-front .divider {
    position: absolute; left: 215px; top: 30px; bottom: 30px; width: 1px; background: var(--rule);
  }
  .details { position: absolute; left: 245px; top: 42px; color: var(--text); }
  .person-name { color: var(--light-blue); font-size: 18px; font-weight: 600; line-height: 1.1; }
  .person-title { font-size: 12.5px; margin-top: 2px; }
  .address { font-size: 12.5px; line-height: 1.5; margin-top: 16px; }
  .contact-list { list-style: none; margin-top: 14px; font-size: 13.5px; line-height: 1.55; }
  .contact-list li { display: flex; align-items: center; gap: 8px; }
  .contact-list svg { width: 11px; height: 11px; fill: var(--light-blue); flex: none; }
  /* Back */
  .card-back .brand {
    position: absolute; left: 0; right: 0; top: 80px; text-align: center;
  }
  .brand-name {
    display: inline-flex; align-items: center; gap: 12px;
    font-size: 54px; font-weight: 700; letter-spacing: 3px; color: var(--silver); line-height: 1;
  }
  .brand-dot { width: 26px; height: 26px; background: var(--silver); border-radius: 50%; }
  .tagline { font-size: 11.5px; letter-spacing: 2.5px; color: var(--gray); margin-top: 8px; text-transform: uppercase; }
  .web-row {
    position: absolute; left: 0; right: 0; top: 196px;
    display: flex; align-items: center; gap: 12px;
  }
  .web-row .line { height: 1px; background: var(--gray); flex: 1; }
  .web-row .line-left { flex: 0 0 180px; }
  .web-row .url { font-size: 11px; color: var(--gray); }
  .web-row .line-right { flex: 0 0 180px; margin-left: auto; opacity: 0; }
</style>
</head>
<body>
<main class="canvas">
  <section class="card card-front">
    <div class="mark-area"><div class="mark-dot" role="img" aria-label="Company mark area"></div></div>
    <div class="divider"></div>
    <div class="details">
      <h1 class="person-name">Marla Drovank</h1>
      <p class="person-title">Office Manager</p>
      <p class="address">1875 W 48TH St Fairbrook<br>Ohio 44102</p>
      <ul class="contact-list">
        <li><svg viewBox="0 0 16 16"><path d="M3 1l3 3-1.5 2c1 2 3 4 5 5L11.5 9.5l3 3L13 15C7 15 1 9 1 3z"/></svg>555.014.2910</li>
        <li><svg viewBox="0 0 16 16"><path d="M4 1h6v4H4zM1 6h14v9H1zm3 3v2h2V9zm4 0v2h2V9z"/></svg>555.014.2971</li>
        <li><svg viewBox="0 0 16 16"><path d="M1 3h14v10H1zm1 1l6 5 6-5z" fill-rule="evenodd"/></svg>mdrovank@kestreltech.com</li>
        <li><svg viewBox="0 0 16 16"><circle cx="8" cy="8" r="7"/></svg>kestreltech.com</li>
      </ul>
    </div>
  </section>

  <section class="card card-back">
    <div class="brand">
      <div class="brand-name">KESTREL<span class="brand-dot"></span></div>
      <p class="tagline">A Cloud Consulting Company</p>
    </div>
    <div class="web-row">
      <span class="line line-left" style="margin-left:150px"></span>
      <span class="url">www.kestreltech.com</span>
    </div>
    <div class="web-row" style="top:260px"><span class="line"></span></div>
  </section>
</main>
</body>
</html>
```